Robotic Physical Therapy office needs a Grand Opening Flyer

We need a Grand Opening flyer design for a robotic physical therapy office named Stellar Motion Therapy. We would like it to have a clean, classy, upscale feeling that gives potential clients a V.I.P. feeling. We would like to use the colors black, gray, and yellow (logo will be uploaded).

Event: Thursday, June 1st, 2023 from 12pm-6pm
location: 58274 Harlow Ave, Bloomfield Hills, MI 48319

Industry/Entity Type

Physical therapy

Font styles to use
Script

Colors

Designer to choose colors to be used in the design.

Requirements
Nice to have
• More of a vip feel for the invite

```html
<!DOCTYPE html>
<html lang="en">
<head>
<meta charset="utf-8">
<title>Stellar Motion Therapy – Grand Opening</title>
<link rel="stylesheet" href="https://fonts.googleapis.com/css2?family=Manrope:wght@500;700;800&family=Cormorant+Garamond:wght@400&family=Great+Vibes&display=swap">
<style>
  :root {
    --page: #ffffff;
    --ink: #0b0b0b;
    --band: #1c1c1c;
    --band-light: #2a2a2a;
    --gold: #f2b233;
    --gold-deep: #a5550c;
    --yellow: #f5d31c;
    --white: #ffffff;
    --rule: rgba(255,255,255,0.55);
  }
  html, body {
    margin: 0;
    width: 1200px;
    height: 1000px;
    overflow: hidden;
    background: var(--page);
  }
  .canvas {
    position: relative;
    width: 1200px;
    height: 1000px;
  }
  .flyer {
    position: absolute;
    left: 270px;
    top: 33px;
    width: 660px;
    height: 934px;
    background: var(--ink);
    overflow: hidden;
    box-shadow: 3px 4px 8px rgba(0,0,0,0.35);
  }
  .flyer-art {
    position: absolute;
    inset: 0;
  }
  .brand {
    position: absolute;
    top: 84px;
    left: 0;
    width: 100%;
    display: flex;
    justify-content: center;
    align-items: center;
    gap: 10px;
  }
  .brand-mark {
    width: 38px;
    height: 38px;
    border-radius: 50%;
    background: var(--yellow);
  }
  .brand-name {
    font-family: "Manrope", sans-serif;
    font-weight: 800;
    font-size: 20px;
    line-height: 1.05;
    color: var(--yellow);
    text-transform: uppercase;
    width: 170px;
  }
  .headline {
    position: absolute;
    left: 0;
    width: 100%;
    text-align: center;
  }
  .headline-grand {
    top: 346px;
    left: 44px;
    font-family: "Cormorant Garamond", serif;
    font-size: 42px;
    letter-spacing: 7px;
    color: var(--white);
  }
  .headline-opening {
    top: 386px;
    font-family: "Great Vibes", cursive;
    font-size: 100px;
    line-height: 1;
    color: var(--yellow);
  }
  .event-details {
    position: absolute;
    left: 0;
    top: 494px;
    width: 100%;
    text-align: center;
    font-family: "Manrope", sans-serif;
    font-weight: 500;
    font-size: 15.5px;
    line-height: 21px;
    color: var(--white);
  }
  .event-details sup { font-size: 9px; }
  .event-rule {
    width: 284px;
    height: 1px;
    background: var(--rule);
    margin: 14px auto 12px;
  }
</style>
</head>
<body>
<div class="canvas">
  <article class="flyer">
    <svg class="flyer-art" viewBox="0 0 660 934" width="660" height="934" aria-hidden="false">
      <defs>
        <linearGradient id="photoTop" x1="0" y1="0" x2="0" y2="1">
          <stop offset="0" stop-color="#4a4d52"/>
          <stop offset="1" stop-color="#1a1b1d"/>
        </linearGradient>
        <linearGradient id="photoFloor" x1="0" y1="0" x2="0" y2="1">
          <stop offset="0" stop-color="#141414"/>
          <stop offset="1" stop-color="#2b2b2b"/>
        </linearGradient>
        <linearGradient id="frameGold" x1="0" y1="1" x2="1" y2="0">
          <stop offset="0" stop-color="var(--gold-deep)"/>
          <stop offset="0.5" stop-color="var(--gold)"/>
          <stop offset="1" stop-color="#c77a14"/>
        </linearGradient>
        <linearGradient id="diamondFill" x1="0" y1="0" x2="0" y2="1">
          <stop offset="0" stop-color="#2a2a2a"/>
          <stop offset="1" stop-color="#141414"/>
        </linearGradient>
        <radialGradient id="ribbonTone">
          <stop offset="0" stop-color="#f0a52a" stop-opacity="0.9"/>
          <stop offset="1" stop-color="#b2620f" stop-opacity="0"/>
        </radialGradient>
        <radialGradient id="glow">
          <stop offset="0" stop-color="#fff6c0"/>
          <stop offset="0.3" stop-color="#f5d31c" stop-opacity="0.7"/>
          <stop offset="1" stop-color="#f5d31c" stop-opacity="0"/>
        </radialGradient>
      </defs>

      <rect class="photo-clinic" x="150" y="0" width="360" height="300" fill="url(#photoTop)" opacity="0.8" role="img" aria-label="Photo of a patient walking in a robotic gait trainer in a clinic"/>
      <rect class="photo-floor" x="120" y="500" width="420" height="434" fill="url(#photoFloor)" role="img" aria-label="Photo of the patient's feet on a treadmill walkway"/>

      <polygon class="band" points="0,0 205,0 330,200 0,200" fill="var(--band)"/>
      <polygon class="band" points="460,0 660,0 660,200 330,200" fill="var(--band)"/>
      <polygon class="band" points="0,200 330,200 60,500 0,500" fill="#121212"/>
      <polygon class="band" points="330,200 660,200 660,500 600,500" fill="#121212"/>
      <polygon class="band-accent" points="0,240 200,0 215,0 0,258" fill="var(--band-light)"/>
      <polygon class="band-accent" points="660,240 470,0 455,0 660,258" fill="var(--band-light)"/>
      <polygon class="band" points="0,500 120,500 120,934 0,934" fill="#0e0e0e"/>
      <polygon class="band" points="540,500 660,500 660,934 540,934" fill="#0e0e0e"/>
      <line x1="0" y1="240" x2="200" y2="0" stroke="var(--gold)" stroke-width="1" opacity="0.6"/>
      <line x1="660" y1="690" x2="470" y2="934" stroke="var(--gold)" stroke-width="1" opacity="0.5"/>

      <polygon class="invite-diamond" points="330,195 602,464 330,737 58,464" fill="url(#diamondFill)" stroke="url(#frameGold)" stroke-width="4"/>

      <ellipse class="ribbon" cx="80" cy="205" rx="50" ry="28" fill="url(#ribbonTone)" role="img" aria-label="Gold curled ribbon"/>
      <ellipse class="ribbon" cx="570" cy="280" rx="80" ry="120" fill="url(#ribbonTone)" role="img" aria-label="Gold curled ribbon"/>
      <ellipse class="ribbon" cx="90" cy="770" rx="70" ry="90" fill="url(#ribbonTone)" role="img" aria-label="Gold curled ribbon"/>
      <ellipse class="ribbon" cx="555" cy="700" rx="60" ry="30" fill="url(#ribbonTone)" role="img" aria-label="Gold curled ribbon"/>

      <circle cx="360" cy="290" r="22" fill="url(#glow)"/>
      <circle cx="440" cy="275" r="30" fill="url(#glow)"/>
      <circle cx="70" cy="370" r="20" fill="url(#glow)"/>
      <circle cx="150" cy="625" r="30" fill="url(#glow)"/>
      <circle cx="545" cy="760" r="22" fill="url(#glow)"/>
      <circle cx="530" cy="65" r="14" fill="url(#glow)"/>
    </svg>

    <header class="brand">
      <span class="brand-mark"></span>
      <span class="brand-name">Stellar Motion Therapy</span>
    </header>

    <div class="headline headline-grand">GRAND</div>
    <div class="headline headline-opening">Opening</div>

    <div class="event-details">
      <div class="event-date">Thursday, June 1<sup>st</sup>,<br>2023 from 12pm - 6pm</div>
      <div class="event-rule"></div>
      <div class="event-address">58274 Harlow Ave, Bloomfield Hills,<br>MI 48319</div>
    </div>
  </article>
</div>
</body>
</html>
```